Bramble Travel Planners needs an bold logo and business card design

Thanks you all for helping me with this project your assistance is appriciated
I am starting a home based travel agency and I need a bold and eye catching logo and business card designed.
I want to convey a sense of FREEDOM, expertise, customer service for travel customers
Bramble travel planners is a full service travel agency focused on customer service and adding value to a vacation and travel planning.
my idea is for a card that looks like an cruise ship boarding pass or passport with stamps with a back drop of beautiful beach scene, resort hotel and happiness.
The logo should be eye catching, unique but give a sense of freedom and it should be travel related
We want to give customers a sense of Freedom from travel planning, freedom from researching cruises and hotels and freedom to enjoy a wonderful cost effective vacation.

Target Market(s)

Customers considering travel for vacations, family reunions, business and weddings

Industry/Entity Type

Travel Industry

Contact Information for Business Card

Bramble Travel Planners
Warren Pelfrey Owner
WPelfrey@BrambleTravelPlanners.com
BrambleTravelPlanners.com
(555) 014-2287

Logo Text

“One’s destination is never a place, but a new way of seeing things.”

Font styles to use
Serif

Colors
85cae6
0492cd
ec1f27
e667a6
b768aa
33b8a4

Requirements
Must have
• The Logo you create should be on the busoness card
• should be clean, easy to read and attractive
• something you that would make you want to work with a travel agent
Nice to have
• should have cruise ship, hotel on the card or something that conveys travel
Should not have
• Should not have the american flag
• no yellow on the card

```html
<!DOCTYPE html>
<html lang="en">
<head>
<meta charset="utf-8">
<title>Bramble Travel Planners – Business Card</title>
<link rel="stylesheet" href="https://fonts.googleapis.com/css2?family=Source+Serif+4:opsz,wght@8..60,400;8..60,600;8..60,700&display=swap">
<style>
  :root {
    --bg: #eeeeee;
    --brand-blue: #0492cd;
    --sky: #85cae6;
    --accent: #e667a6;
    --accent-strong: #ec1f27;
    --white: #ffffff;
    --water-light: #6fd0f2;
    --water-deep: #1fa9e0;
    --deck: #f4f4f2;
    --card-shadow: 0 6px 14px rgba(0,0,0,0.28);
  }
  * { box-sizing: border-box; margin: 0; padding: 0; }
  html, body {
    width: 1200px; height: 1000px; overflow: hidden;
    background: var(--bg);
    font-family: "Source Serif 4", Georgia, serif;
  }
  .canvas { position: relative; width: 1200px; height: 1000px; }

  /* Contact side */
  .card-contact {
    position: absolute; left: 430px; top: 48px;
    width: 690px; height: 395px;
    background: var(--brand-blue);
    box-shadow: var(--card-shadow);
    color: var(--white);
  }
  .brand-frame {
    position: absolute; left: 55px; top: 138px;
    width: 202px; height: 146px;
    border: 3px solid var(--sky);
  }
  .brand-lockup {
    position: absolute; left: 42px; top: 180px;
    display: flex; align-items: flex-start; gap: 10px;
    font-weight: 700; line-height: 1;
  }
  .brand-lockup .brand-square {
    width: 20px; height: 20px; margin-top: 8px;
    background: var(--accent); flex: none;
  }
  .brand-lockup .brand-name { font-size: 44px; letter-spacing: -0.5px; }
  .brand-lockup .brand-sub {
    display: block; font-size: 20px; font-weight: 400;
    margin-top: 6px; text-align: right;
  }

  .contact-block { position: absolute; left: 276px; top: 138px; }
  .person-name { font-size: 31px; font-weight: 700; }
  .person-role { font-size: 21px; color: var(--sky); margin-top: 2px; }
  .contact-line {
    display: flex; align-items: center; gap: 14px;
    font-size: 18px; margin-top: 10px;
  }
  .contact-line svg { flex: none; }

  /* Photo side */
  .card-photo {
    position: absolute; left: 48px; top: 470px;
    width: 720px; height: 410px;
    box-shadow: var(--card-shadow);
    overflow: hidden;
  }
  .photo-fill {
    position: absolute; inset: 0;
    background: linear-gradient(180deg, var(--water-light) 0%, var(--water-deep) 58%, #b55a45 60%, var(--deck) 62%, #e6e6e4 100%);
  }
  .web-tag {
    position: absolute; left: 222px; top: 335px;
    background: var(--accent-strong); color: var(--white);
    font-size: 22px; padding: 3px 14px;
  }

  /* Standalone logo */
  .logo-standalone {
    position: absolute; left: 862px; top: 762px;
    width: 296px; height: 190px;
  }
  .logo-standalone .brand-frame {
    left: 20px; top: 0; width: 276px; height: 190px;
    border-color: var(--brand-blue);
  }
  .logo-standalone .brand-lockup { left: 0; top: 48px; color: var(--brand-blue); }
  .logo-standalone .brand-name { font-size: 60px; }
  .logo-standalone .brand-sub { font-size: 28px; }
  .logo-standalone .brand-square { width: 24px; height: 24px; margin-top: 12px; }
</style>
</head>
<body>
<main class="canvas">

  <section class="card-contact">
    <div class="brand-frame"></div>
    <div class="brand-lockup">
      <span class="brand-square"></span>
      <span class="brand-name">Bramble<span class="brand-sub">Travel Planners</span></span>
    </div>
    <div class="contact-block">
      <div class="person-name">Warren Pelfrey</div>
      <div class="person-role">Owner</div>
      <div class="contact-line">
        <svg width="24" height="18" viewBox="0 0 24 18" aria-hidden="true">
          <rect x="1" y="1" width="22" height="16" fill="none" stroke="#85cae6" stroke-width="2"/>
          <path d="M1 1 L12 10 L23 1 M1 17 L9 8 M23 17 L15 8" fill="none" stroke="#85cae6" stroke-width="2"/>
        </svg>
        <span>WPelfrey@BrambleTravelPlanners.com</span>
      </div>
      <div class="contact-line">
        <svg width="24" height="26" viewBox="0 0 24 26" aria-hidden="true">
          <rect x="6" y="1" width="12" height="24" rx="2" fill="none" stroke="#85cae6" stroke-width="2"/>
          <rect x="9" y="5" width="6" height="13" fill="#85cae6"/>
          <circle cx="12" cy="21" r="1.4" fill="#85cae6"/>
        </svg>
        <span>(555) 014-2287</span>
      </div>
    </div>
  </section>

  <section class="card-photo">
    <div class="photo-fill" role="img" aria-label="Photo of a woman in a wide striped sun hat resting her arms on the edge of a blue swimming pool beside a white wooden deck"></div>
    <div class="web-tag">BrambleTravelPlanners.com</div>
  </section>

  <aside class="logo-standalone">
    <div class="brand-frame"></div>
    <div class="brand-lockup">
      <span class="brand-square"></span>
      <span class="brand-name">Bramble<span class="brand-sub">Travel Planners</span></span>
    </div>
  </aside>

</main>
</body>
</html>
```